Re-design existing website and add products for sale.

Our current website is very basic and cluttered. (brightwillowcare.com.au)We want a modern looking website that is easy to navigate. We also want to start selling essential oils and crystal products, so there needs to be a separate page for this. Also needs to be easily edited as we need to change the monthly oracle card with the description. Would like calming colours as we are all about natural healing. Alongside the services listed there should be a button to book now which asks for their name, email, phone number ect. and adds it to the cart.

• Logo is still being designed, please leave a space for the logo which will basically be a lotus flower within a mandala.

```html
<!DOCTYPE html>
<html lang="en">
<head>
<meta charset="utf-8">
<title>Bright Willow Care – Services</title>
<link rel="stylesheet" href="https://fonts.googleapis.com/css2?family=Amaranth:ital,wght@1,400&family=Cabin:wght@700&display=swap">
<style>
  :root {
    --cream: #fefdf0;
    --card: #ffffff;
    --gold: #cc8f35;
    --ink: #1c1c1c;
    --line-gold: #e4c48e;
  }
  * { margin: 0; padding: 0; box-sizing: border-box; }
  html, body { width: 1200px; height: 1000px; overflow: hidden; }
  body {
    position: relative;
    background: var(--cream);
    font-family: "Amaranth", "Trebuchet MS", sans-serif;
    color: var(--ink);
  }
  .lotus-field {
    position: absolute;
    left: 0; top: 380px;
    width: 1200px; height: 620px;
    background: linear-gradient(to bottom, rgba(254,253,240,0) 0%, rgba(240,220,180,0.35) 45%, rgba(228,196,142,0.45) 100%);
  }
  .service-card {
    position: absolute;
    top: -20px;
    width: 287px;
    background: var(--card);
    box-shadow: 0 2px 6px rgba(0,0,0,0.18);
  }
  .service-card--healing { left: 140px; height: 990px; }
  .service-card--workshops { left: 457px; height: 738px; }
  .service-card--oracle { left: 773px; height: 371px; }
  .service-text {
    position: absolute;
    top: 20px; left: 0; right: 0;
    text-align: center;
    font-style: italic;
    font-size: 19px;
    line-height: 22.9px;
    letter-spacing: -0.1px;
  }
  .price-button {
    position: absolute;
    left: 30px;
    width: 227px; height: 60px;
    background: var(--gold);
    color: #fff;
    font-family: "Cabin", Arial, sans-serif;
    font-weight: 700;
    font-size: 17px;
    line-height: 24px;
    display: flex; flex-direction: column;
    align-items: center; justify-content: center;
    text-align: center;
  }
  .service-card--healing .price-button { top: 910px; }
  .service-card--workshops .price-button { top: 658px; width: 226px; font-size: 18px; line-height: 25px; }
  .service-card--oracle .price-button { top: 291px; }
</style>
</head>
<body>
  <div class="lotus-field" role="img" aria-label="Line illustration of lotus flowers, buds and seed pods in gold outline"></div>

  <section class="service-card service-card--healing">
    <p class="service-text">
      wonderful hands-on healing<br>technique, which can help<br>boost and balance your<br>energy levels, strengthen<br>your immune system, help<br>you relax and let go of stress<br>and tension and help to<br>maintain your overall health<br>and wellbeing. It can help<br>clear blockages and clear<br>past lives and is a great<br>technique for cleansing the<br>body and breaking down<br>stale energy blockages.<br><br>
      Seichim is an ancient and<br>sacred healing modality. It is<br>an advanced form of healing<br>which involves the use of<br>sacred geometry symbols<br>using two hands. It helps<br>clear past lives in a different<br>way to Reiki and helps<br>release blockages from your<br>energy field. It is a form of<br>healing which has been<br>taught in many mystery<br>schools in ancient times.<br>Seichim is said to be the<br>parent energy of all hands-on<br>healing systems and is<br>believed to have originated<br>from Atlantean times. It can<br>be shown that Seichim was<br>practiced by the Mayan<br>civilisation in South America<br>before being introduced to<br>Egypt.
    </p>
    <div class="price-button"><span>1 Hour - $75</span><span>1/2 Hour - $40</span></div>
  </section>

  <section class="service-card service-card--workshops">
    <p class="service-text">
      Life Force Energy.<br>Rei = Universal<br>Ki = Vital Energy<br><br>
      Would you like to feel more<br>grounded, self empowered,<br>confident and relaxed?<br><br>
      Have you had the chance to<br>experience Reiki or Seichim<br>and now wish to further your<br>knowledge of these ancient<br>healing techniques and use<br>them to help yourself and<br>others around you?<br><br>
      I offer Reiki 1 &amp; 2 workshops<br>as well as Seichim workshops<br>where I work one on one with<br>you to teach you these<br>wonderful techniques.<br><br>
      Prerequisites:<br>Reiki 1 - None<br>Reiki 2 - Reiki 1 Certificate<br>Isis Seichim - Reiki 1 &amp; 2<br>Certificates
    </p>
    <div class="price-button"><span>Reiki 1 Workshop - $180</span><span>Reiki 2 Workshop - $280</span></div>
  </section>

  <section class="service-card service-card--oracle">
    <p class="service-text">
      wisdom cards are cards used<br>for divination, fortune telling<br>and spiritual guidance.<br><br>
      Oracle cards are the modern<br>version of tarot cards, which<br>have been used for centuries<br>by people to find meaningful<br>answers to questions about<br>their life, spiritual path and<br>future.
    </p>
    <div class="price-button"><span>20 Minutes - $30</span></div>
  </section>
</body>
</html>
```